Elmrow Management real estate management company needs presentation folder to hand clients

looking for a folder with pockets that represent my real estate management company when i hand to client reports or promotional material. I only do resedential real estate. I want classy and professional - pictures or additioal graphixs are fine

when a client open i will usally insert text and reports about my business
also on the inside flap is usally place for my business card i will upload a picture so the theme can be constant

Target Market(s)

my existing real estate cleints
and i will use when i am soliciting new business

Industry/Entity Type

Real Estate

Font styles to use
Serif

Requirements
Must have
• must have logo
• must give appearance of professionalism and maturity
• have basic company info tel# ,address
• id like viewer to know I manage real estate - focus on residential small to large apartment buildings
• not strip malls, not giganic complexes - im a mid size company
• logo is black but i welcome color as u see fit
Nice to have
• maybe pictures
• my slogan - " we will manage your building like its our own "
• focus on professioanl, safe, trust worthy
• type style should be clear and readable - but im open to sugestions

```html
<!DOCTYPE html>
<html lang="en">
<head>
<meta charset="utf-8">
<title>Elmrow Management — Presentation Folder</title>
<link rel="stylesheet" href="https://fonts.googleapis.com/css2?family=Montserrat:wght@400;500;700;800&family=Open+Sans:wght@400&family=Archivo:wght@400;800&display=swap">
<style>
  :root {
    --ink: #1a1a1a;
    --white: #ffffff;
    --sky-top: #8fbde6;
    --sky-light: #c9e2f4;
    --shade: #2a2c30;
    --pocket: #e9eaec;
    --card-frame: #050505;
    --crop: #c2257a;
    --rule: #d9d9d9;
  }
  * { box-sizing: border-box; margin: 0; padding: 0; }
  html, body { width: 1200px; height: 1101px; overflow: hidden; background: var(--white); }
  body { position: relative; font-family: "Montserrat", sans-serif; color: var(--ink); }

  .folder-cover { position: absolute; left: 100px; top: 76px; width: 996px; height: 694px; overflow: hidden; }
  .cover-photo, .cover-shapes { position: absolute; inset: 0; }

  .contact-block {
    position: absolute; left: 64px; top: 42px;
    font-family: "Open Sans", sans-serif; font-size: 16px; line-height: 21px; color: #1c2a3a;
  }

  .brand-mark {
    position: absolute; left: 852px; top: 86px; width: 124px;
    display: flex; align-items: center; gap: 7px;
    font-family: "Montserrat", sans-serif; font-weight: 700; font-size: 12px; line-height: 15px;
    letter-spacing: 1px; color: var(--ink); text-transform: uppercase;
  }
  .brand-mark .brand-square { flex: none; width: 10px; height: 10px; background: var(--ink); }

  .slogan { position: absolute; left: 587px; top: 472px; width: 316px; color: var(--white); text-align: center; white-space: nowrap; }
  .slogan .rule { height: 1px; background: var(--rule); }
  .slogan .lead { font-weight: 500; font-size: 21px; letter-spacing: 1px; line-height: 34px; }
  .slogan .key { font-weight: 800; font-size: 34px; line-height: 42px; margin-top: 3px; }
  .slogan .close { font-weight: 500; font-size: 28px; line-height: 34px; letter-spacing: 0.5px; }

  .pocket { position: absolute; left: 0; top: 0; }

  .business-card { position: absolute; left: 223px; top: 819px; width: 219px; height: 132px; background: var(--card-frame); }
  .business-card .card-face {
    position: absolute; left: 12px; top: 10px; right: 12px; bottom: 11px; background: var(--white);
    font-family: "Archivo", sans-serif; color: var(--ink);
  }
  .card-brand {
    position: absolute; left: 8px; top: 32px; width: 78px;
    font-family: "Montserrat", sans-serif; font-weight: 700; font-size: 7px; letter-spacing: 0.5px;
    text-transform: uppercase; text-align: center; line-height: 10px;
  }
  .card-divider { position: absolute; left: 90px; top: 26px; width: 1px; height: 46px; background: var(--ink); }
  .card-details { position: absolute; right: 10px; top: 28px; text-align: right; line-height: 6px; font-size: 5.5px; white-space: nowrap; }
  .card-details .name { font-weight: 800; font-size: 11px; line-height: 12px; letter-spacing: -0.3px; }
  .card-details .title { font-size: 5.5px; margin-bottom: 5px; }
  .card-details .address { font-size: 3.5px; line-height: 5px; }
  .card-tagline {
    position: absolute; left: 8px; right: 8px; top: 93px;
    display: flex; align-items: center; gap: 4px; font-size: 4.5px; white-space: nowrap;
  }
  .card-tagline::before, .card-tagline::after { content: ""; flex: 1; height: 0.5px; background: #999; }
  .crop-marks { position: absolute; left: 0; top: 0; pointer-events: none; }
</style>
</head>
<body>

<section class="folder-cover">
  <svg class="cover-photo" role="img" aria-label="Photograph of a modern white and dark residential building against a blue sky" width="996" height="694" viewBox="0 0 996 694">
    <defs>
      <linearGradient id="sky" x1="0" y1="0" x2="1" y2="0.25">
        <stop offset="0" stop-color="#8fbde6"/>
        <stop offset="0.55" stop-color="#c9e2f4"/>
        <stop offset="0.85" stop-color="#ffffff"/>
      </linearGradient>
      <linearGradient id="building" x1="0" y1="0" x2="0" y2="1">
        <stop offset="0" stop-color="#d9dcdf"/>
        <stop offset="0.35" stop-color="#5b5e63"/>
        <stop offset="1" stop-color="#2b2d31"/>
      </linearGradient>
    </defs>
    <rect width="996" height="694" fill="url(#sky)"/>
    <rect x="0" y="200" width="996" height="494" fill="url(#building)"/>
  </svg>

  <svg class="cover-shapes" width="996" height="694" viewBox="0 0 996 694" aria-hidden="true">
    <polygon points="92,137 750,137 630,208 216,208" fill="#ffffff" opacity="0.35"/>
    <polygon points="92,137 430,694 0,694 0,137" fill="#9aa3ad" opacity="0.25"/>
    <polygon points="996,200 996,694 730,694 900,240" fill="#8a8f96" opacity="0.35"/>
    <polygon points="420,370 650,294 996,430 996,694 480,694" fill="#2a2c30" opacity="0.45"/>
  </svg>

  <div class="contact-block">
    <p>phone: 914-555-0142</p>
    <p>email: dreyes@elmrowmail.com</p>
    <p>cell: 917-555-0187</p>
  </div>

  <div class="brand-mark"><span class="brand-square"></span><span>Elmrow Management</span></div>

  <div class="slogan">
    <div class="rule"></div>
    <p class="lead">WE WILL MANAGE</p>
    <div class="rule"></div>
    <p class="key">YOUR BUILDING</p>
    <p class="close">LIKE IT IS OUR OWN</p>
  </div>
</section>

<svg class="pocket" width="1200" height="1101" viewBox="0 0 1200 1101" aria-hidden="true">
  <path d="M100,770 L66,801 L66,988 L100,999 L577,999 Q585,999 585,991 L585,770 Z" fill="var(--pocket)"/>
</svg>

<div class="business-card">
  <div class="card-face">
    <div class="card-brand">Elmrow<br>Management</div>
    <div class="card-divider"></div>
    <div class="card-details">
      <p class="name">Daniel Reyes</p>
      <p class="title">MASTER BUILDING MANAGER</p>
      <p>office tel 914-555-0142</p>
      <p>email dreyes@elmrowmail.com</p>
      <p>cell 917-555-0187</p>
      <p class="address">12 LINDEN PLACE SUITE 4 ALDER FALLS NY 10599</p>
    </div>
    <p class="card-tagline">WE WILL MANAGE YOUR BUILDING LIKE IT IS OUR OWN</p>
  </div>
</div>

<svg class="crop-marks" width="1200" height="1101" viewBox="0 0 1200 1101" aria-hidden="true">
  <line x1="215" y1="859" x2="261" y2="815" stroke="var(--crop)" stroke-width="0.8"/>
  <line x1="403" y1="954" x2="449" y2="910" stroke="var(--crop)" stroke-width="0.8"/>
</svg>

</body>
</html>
```